Energy trading company (Voltrisa) needs a business card

We need a business card for a company based in Central America. Our main purpose is trading energy . We already have the logo but we need some good creativity to design a high impact business card. Colors blue, orange, green can be used or we would like to see good combinatios with our logo

Target Market(s)

Energy

Industry/Entity Type

Power Generation

Contact Information for Business Card

Logo , headquarters , name, background

Font styles to use
Serif
Sans Serif

Colors

Designer to choose colors to be used in the design.

Requirements
Must have
• it must have a fresh and clean view
Nice to have
• good backgrounds that combine with the logo
Should not have
• too much words

```html
<!DOCTYPE html>
<html lang="en">
<head>
<meta charset="utf-8">
<title>Voltrisa Business Card</title>
<link rel="stylesheet" href="https://fonts.googleapis.com/css2?family=Montserrat:wght@400;500;700&display=swap">
<style>
  :root {
    --stage: #4b4b4d;
    --orange: #f7931e;
    --orange-deep: #e07b12;
    --orange-light: #fbb061;
    --white: #ffffff;
    --shadow: rgba(0, 0, 0, 0.35);
  }
  * { margin: 0; padding: 0; box-sizing: border-box; }
  html, body {
    width: 1200px;
    height: 1200px;
    overflow: hidden;
    background: var(--stage);
    font-family: "Montserrat", Arial, sans-serif;
  }
  .stage {
    position: relative;
    width: 1200px;
    height: 1200px;
  }
  .card {
    position: absolute;
    left: 150px;
    width: 900px;
    height: 514px;
    box-shadow: 0 14px 30px var(--shadow);
    overflow: hidden;
  }
  /* Front */
  .card-front {
    top: 56px;
    background: var(--orange);
  }
  .front-tone {
    position: absolute;
    left: 0;
    top: 0;
    width: 470px;
    height: 100%;
    background: linear-gradient(90deg, var(--orange) 0%, var(--orange-deep) 35%, var(--orange-light) 100%);
    opacity: 0.55;
  }
  .front-name {
    position: absolute;
    right: 60px;
    bottom: 150px;
    color: var(--white);
    font-size: 62px;
    font-weight: 500;
    letter-spacing: 1px;
    text-transform: uppercase;
  }
  /* Back */
  .card-back {
    top: 630px;
    background: var(--white);
  }
  .brand {
    position: absolute;
    left: 60px;
    top: 150px;
    width: 380px;
    text-align: center;
    color: var(--orange);
  }
  .brand-dot {
    width: 70px;
    height: 70px;
    margin: 0 auto 14px;
    border-radius: 50%;
    background: var(--orange);
  }
  .brand-name {
    font-size: 62px;
    font-weight: 400;
    letter-spacing: 1px;
    text-transform: uppercase;
    line-height: 1;
  }
  .divider {
    position: absolute;
    left: 470px;
    top: 140px;
    width: 3px;
    height: 200px;
    background: var(--orange);
  }
  .contact {
    position: absolute;
    left: 510px;
    top: 140px;
    color: var(--orange);
  }
  .person-name {
    font-size: 28px;
    font-weight: 700;
    letter-spacing: 1px;
    text-transform: uppercase;
    line-height: 1.1;
  }
  .person-role {
    font-size: 20px;
    font-weight: 500;
    margin-bottom: 18px;
  }
  .address {
    font-size: 20px;
    line-height: 1.2;
    margin-bottom: 16px;
  }
  .contact-list { list-style: none; }
  .contact-list li {
    display: flex;
    align-items: center;
    gap: 14px;
    font-size: 21px;
    line-height: 1.45;
  }
  .contact-icon {
    width: 18px;
    height: 18px;
    flex: none;
    fill: var(--orange);
  }
</style>
</head>
<body>
<main class="stage">
  <section class="card card-front" aria-label="Card front">
    <div class="front-tone"></div>
    <p class="front-name">Voltrisa</p>
  </section>

  <section class="card card-back" aria-label="Card back">
    <div class="brand">
      <div class="brand-dot"></div>
      <p class="brand-name">Voltrisa</p>
    </div>
    <div class="divider"></div>
    <div class="contact">
      <p class="person-name">Dana Roulet</p>
      <p class="person-role">Manager</p>
      <p class="address">Your address, city<br>state, ZIP 0000</p>
      <ul class="contact-list">
        <li>
          <svg class="contact-icon" viewBox="0 0 24 24" aria-hidden="true"><path d="M6.6 10.8a15 15 0 0 0 6.6 6.6l2.2-2.2c.3-.3.7-.4 1-.2 1.1.4 2.3.6 3.6.6.6 0 1 .4 1 1V20c0 .6-.4 1-1 1C10.6 21 3 13.4 3 4c0-.6.4-1 1-1h3.5c.6 0 1 .4 1 1 0 1.3.2 2.5.6 3.6.1.3 0 .7-.2 1z"/></svg>
          123-456-2100
        </li>
        <li>
          <svg class="contact-icon" viewBox="0 0 24 24" aria-hidden="true"><path d="M2 5h20v14H2z M3.5 6.5 12 13l8.5-6.5" fill="none" stroke="#f7931e" stroke-width="2"/><path d="M2 5h20l-10 8z"/></svg>
          youremail@mailbox.com
        </li>
        <li>
          <svg class="contact-icon" viewBox="0 0 24 24" aria-hidden="true"><circle cx="12" cy="12" r="10"/><path d="M2 12h20M12 2c3 3 3 17 0 20M12 2c-3 3-3 17 0 20" fill="none" stroke="#ffffff" stroke-width="1.5"/></svg>
          www.yourwebsite.com
        </li>
      </ul>
    </div>
  </section>
</main>
</body>
</html>
```